We need to design Labels of one of Our Brand QuelaVant Lotion.

The purpose of this product is to keep mosquitoes away.
There are 3 variants of this lotion. So we need 3 designs for the product. These variants details are mentioned below:

1) Mosquito Repellent Lotion with Lavender Fragrance.
2) Mosquito Repellent Lotion with Natural Ingredients.
3) Mosquito Repellent Lotion for kids.

Kindly note the bottle will be WHITE for all the variants. Cap will of the bottle will be with accordance to the color of label. In the picture it is red just for presentation.

Kindly share design of Repellent Lotion with Lavendar Fragrance initially and if we give your positive feedback, then you may add further variants of the design.

The bottle shape is attached along with keylines. Also attaching logo. If there is any other option for logo, you can suggest which we would probably keep our existing logo.

Target Market(s)

B+, B, C+

Industry/Entity Type

Product

Colors
a54499
6b449b

Requirements
Must have
• Mosquito
• 100ml
Nice to have
• Purple color as background
Should not have
• Lavendar flower

```html
<!DOCTYPE html>
<html lang="en">
<head>
<meta charset="utf-8">
<title>QuelaVant Mosquito Repellent Lotion – Lavender Label</title>
<link href="https://fonts.googleapis.com/css2?family=Ubuntu:wght@700&family=Roboto+Condensed:wght@500&display=swap" rel="stylesheet">
<style>
  :root {
    --page-bg: #e4e4e4;
    --label-purple: #5a2a8e;
    --label-purple-light: #6b449b;
    --label-purple-dark: #4a1f7c;
    --accent-magenta: #a54499;
    --headline-yellow: #fff200;
    --text-lilac: #e6dcf5;
    --text-white: #ffffff;
  }
  * { margin: 0; padding: 0; box-sizing: border-box; }
  html, body {
    width: 1200px;
    height: 1159px;
    overflow: hidden;
    background: var(--page-bg);
  }
  .label {
    position: absolute;
    left: 320px;
    top: 40px;
    width: 560px;
    height: 1080px;
    border-radius: 28px;
    overflow: hidden;
    background: linear-gradient(180deg, var(--label-purple) 0%, var(--label-purple-light) 55%, var(--label-purple-dark) 100%);
  }
  .emblem-area {
    position: absolute;
    left: 140px;
    top: 380px;
    width: 400px;
    height: 560px;
    border-radius: 50%;
    background: radial-gradient(ellipse at center, rgba(74, 31, 124, 0.55) 0%, rgba(74, 31, 124, 0.25) 60%, rgba(74, 31, 124, 0) 75%);
  }
  .brand {
    position: absolute;
    left: 0;
    top: 140px;
    width: 100%;
    display: flex;
    align-items: center;
    justify-content: center;
    gap: 18px;
  }
  .brand-dot {
    width: 26px;
    height: 26px;
    border-radius: 50%;
    background: var(--accent-magenta);
  }
  .brand-name {
    font-family: "Ubuntu", sans-serif;
    font-weight: 700;
    font-size: 78px;
    color: var(--text-white);
    letter-spacing: 1px;
  }
  .product-title {
    position: absolute;
    left: 62px;
    top: 470px;
    font-family: "Ubuntu", sans-serif;
    font-weight: 700;
    font-size: 78px;
    line-height: 92px;
    color: var(--headline-yellow);
  }
  .variant {
    position: absolute;
    left: 64px;
    top: 770px;
    font-family: "Roboto Condensed", sans-serif;
    font-weight: 500;
    font-size: 31px;
    color: var(--text-lilac);
    letter-spacing: 0.5px;
  }
  .volume {
    position: absolute;
    left: 0;
    width: 100%;
    top: 995px;
    text-align: center;
    font-family: "Roboto Condensed", sans-serif;
    font-weight: 500;
    font-size: 30px;
    color: var(--text-white);
  }
</style>
</head>
<body>
  <main class="label">
    <div class="emblem-area" role="img" aria-label="Faint background emblem of a crossed-out mosquito"></div>

    <div class="brand">
      <span class="brand-dot"></span>
      <span class="brand-name">QuelaVant</span>
    </div>

    <h1 class="product-title">Mosquito<br>Repellent<br>Lotion</h1>
    <p class="variant">with Lavender Fragrance</p>
    <p class="volume">100ml</p>
  </main>
</body>
</html>
```